Nobre Lente Lusitana - business card

Create a business card for my eyewear (glasses) store. The concept is based in handcrafted glasses (as well as common frames and 3d printed), clean, and elegant. The business card could be black (white letters and symbols) or white (black letters and symbols) but we are open to new suggestions. It must be sober and elegant.
The name Nobre Lente Lusitana means Royal/Real Portuguese Optical Store.
Our concept should be inspired by the pictures attatched bellow.
I would like it to be classic and elegant as business cards for bankers.
Our first selected logo is also available in attachment files.

Target Market(s)

For business meetings with investors, supliers and fairs

Industry/Entity Type

Eyewear

Contact Information for Business Card

Some random business cards in attachment that we like. Don't be closed to it, we like freedom of think.

Font styles to use
Serif
Sans Serif

Colors
404040
e9e9e9
fbfbfb
000000
85abd3
0255a3
f7fbfd
959595

Requirements
Must have
• Must be elegant, simple.
• Must present our brand new logo (slight variations are welcome, the logo is not closed yet). See our temporary logo in attachment.
• Black (or dark grey), white (or light grey) and a third slight color.
• This third slight color could be dark blue or grayish blue.
• Info:
• Tomás Vidigal (name)
• tvidigal@nobrelentelusitana.example
• +351 927364051
• www.nobrelentelusitana.example
Nice to have
• Black and white or with serious colors such as dark blue or greyish blue.
• Could also have water mark with our logo (big size) in the background (inspired in KMT bank credit card design)
Should not have
• Hysteric colora or shapes

```html
<!DOCTYPE html>
<html lang="pt">
<head>
<meta charset="utf-8">
<title>Nobre Lente Lusitana – Business Card</title>
<link href="https://fonts.googleapis.com/css2?family=Bebas+Neue&family=Jost:wght@400&family=Open+Sans:wght@400&display=swap" rel="stylesheet">
<style>
  :root {
    --backdrop: #e9e9e9;
    --card: #222222;
    --ink: #fbfbfb;
    --rule: #e9e9e9;
    --mark-area: #2e2e2e;
  }
  * { margin: 0; padding: 0; box-sizing: border-box; }
  html, body { width: 1200px; height: 1000px; overflow: hidden; }
  body {
    position: relative;
    background: var(--backdrop);
    font-family: "Open Sans", sans-serif;
    color: var(--ink);
  }
  .card {
    position: absolute;
    left: 267px;
    width: 665px;
    height: 397px;
    background: var(--card);
    border-radius: 24px;
  }
  .card--front { top: 75px; }
  .card--back { top: 533px; }

  .brand-mark {
    position: absolute;
    left: 203px;
    top: 75px;
    width: 260px;
    height: 160px;
    background: var(--mark-area);
    border-radius: 6px;
  }
  .brand {
    position: absolute;
    left: 0; right: 0;
    top: 262px;
    text-align: center;
    font-family: "Jost", sans-serif;
    font-weight: 400;
    text-transform: uppercase;
  }
  .brand__main {
    font-size: 32px;
    line-height: 38px;
    letter-spacing: 2px;
  }
  .brand__sub {
    font-size: 19px;
    line-height: 24px;
    letter-spacing: 2.5px;
  }

  .identity {
    position: absolute;
    right: 398px;
    top: 168px;
    text-align: right;
  }
  .identity__name {
    font-family: "Bebas Neue", sans-serif;
    font-size: 27px;
    line-height: 30px;
    letter-spacing: 0.3px;
  }
  .identity__role {
    font-size: 15px;
    line-height: 22px;
  }
  .divider {
    position: absolute;
    left: 286px;
    top: 168px;
    width: 1px;
    height: 58px;
    background: var(--rule);
  }
  .contacts {
    position: absolute;
    left: 302px;
    top: 165px;
    list-style: none;
    font-size: 15px;
    line-height: 21px;
  }
  .contacts li { display: flex; align-items: center; gap: 7px; }
  .contacts svg { width: 14px; height: 14px; flex: none; }
</style>
</head>
<body>
  <section class="card card--front">
    <div class="brand-mark" role="img" aria-label="Brand mark area for the Nobre Lente Lusitana logo"></div>
    <div class="brand">
      <div class="brand__main">Nobre Lente</div>
      <div class="brand__sub">Lusitana</div>
    </div>
  </section>

  <section class="card card--back">
    <div class="identity">
      <div class="identity__name">Tomás Vidigal</div>
      <div class="identity__role">Managing Partner</div>
    </div>
    <div class="divider"></div>
    <ul class="contacts">
      <li>
        <svg viewBox="0 0 24 24" fill="none" stroke="currentColor" stroke-width="1.8" stroke-linejoin="round"><path d="M5 3h4l2 5-2.5 1.5a11 11 0 0 0 6 6L16 13l5 2v4a2 2 0 0 1-2 2A16 16 0 0 1 3 5a2 2 0 0 1 2-2z"/></svg>
        +351 927364051
      </li>
      <li>
        <svg viewBox="0 0 24 24" fill="none" stroke="currentColor" stroke-width="1.8"><rect x="3" y="5" width="18" height="14" rx="1"/><path d="M3 6l9 7 9-7"/></svg>
        tvidigal@nobrelentelusitana.example
      </li>
      <li>
        <svg viewBox="0 0 24 24" fill="none" stroke="currentColor" stroke-width="1.6"><circle cx="12" cy="12" r="9"/><path d="M3 12h18M12 3c3 3 3 15 0 18M12 3c-3 3-3 15 0 18"/></svg>
        www.nobrelentelusitana.example
      </li>
    </ul>
  </section>
</body>
</html>
```